Wholesale Fashion Agent

Industry/Entity Type

Fashion

Contact Information for Business Card

I have attached the previous logo, we are wanting to re-vamp with black and white only. Sharp and more modern.

Mirela Stonecroft Agencies back of card
address (to be advised, as we are moving)

MS Agencies front of card, with Fashion Agent on the front

```html
<!DOCTYPE html>
<html lang="en">
<head>
<meta charset="utf-8">
<title>Mirela Stonecroft Agencies – Business Card</title>
<link rel="stylesheet" href="https://fonts.googleapis.com/css2?family=Cormorant+Garamond:wght@500;600&family=Jost:wght@400&family=Tinos&display=swap">
<style>
  :root {
    --ink: #2b2a29;
    --paper: #ffffff;
    --backdrop: #efece6;
    --edge: #d9d6d0;
  }
  * { margin: 0; padding: 0; box-sizing: border-box; }
  html, body { width: 1019px; height: 1200px; overflow: hidden; }
  body { background: var(--backdrop); position: relative; color: var(--ink); }

  .card {
    position: absolute;
    width: 740px;
    height: 457px;
    background: var(--paper);
    border: 1px solid var(--edge);
    overflow: hidden;
  }
  .card--front { left: 135px; top: 98px; }
  .card--back  { left: 131px; top: 655px; width: 741px; }

  .band { position: absolute; top: 0; bottom: 0; background: var(--ink); }
  .card--front .band--wide { left: 0; width: 200px; }
  .card--front .band--thin { left: 206px; width: 8px; }
  .card--back .band--wide { right: 0; width: 107px; }
  .card--back .band--thin { right: 111px; width: 7px; }

  .mark-tile {
    position: absolute;
    background: var(--paper);
    display: flex; align-items: center; justify-content: center;
    font-family: "Cormorant Garamond", serif;
    font-weight: 600;
    color: var(--ink);
  }
  .card--front .mark-tile { left: 117px; top: 152px; width: 98px; height: 150px; font-size: 52px; }
  .card--back .mark-tile  { right: 52px; top: 160px; width: 86px; height: 107px; font-size: 44px; }

  .identity {
    position: absolute;
    left: 262px; top: 186px;
    width: 400px;
    text-align: center;
  }
  .identity__name {
    font-family: "Cormorant Garamond", serif;
    font-weight: 500;
    font-variant: small-caps;
    font-size: 46px;
    line-height: 1;
    letter-spacing: 0.5px;
    white-space: nowrap;
  }
  .identity__role {
    margin-top: 14px;
    font-family: "Jost", sans-serif;
    font-size: 26px;
    letter-spacing: 4px;
  }

  .company {
    position: absolute;
    left: 56px; top: 82px;
    font-family: "Cormorant Garamond", serif;
    font-weight: 500;
    font-variant: small-caps;
    font-size: 30px;
    line-height: 1;
    padding-bottom: 4px;
    border-bottom: 2px solid var(--ink);
    white-space: nowrap;
  }

  .contacts {
    position: absolute;
    left: 50px; top: 164px;
    list-style: none;
    font-family: "Tinos", serif;
    font-size: 23px;
  }
  .contacts li {
    display: flex; align-items: center;
    height: 35px;
    white-space: nowrap;
  }
  .contacts svg { width: 24px; height: 20px; margin-right: 8px; flex: none; }
</style>
</head>
<body>

<section class="card card--front" aria-label="Front of card">
  <div class="band band--wide"></div>
  <div class="band band--thin"></div>
  <div class="mark-tile">MS</div>
  <div class="identity">
    <h1 class="identity__name">Mirela Stonecroft</h1>
    <p class="identity__role">FASHION AGENT</p>
  </div>
</section>

<section class="card card--back" aria-label="Back of card">
  <div class="band band--wide"></div>
  <div class="band band--thin"></div>
  <div class="mark-tile">MS</div>

  <h2 class="company">Mirela Stonecroft Agencies</h2>

  <ul class="contacts">
    <li>
      <svg viewBox="0 0 24 20" aria-hidden="true"><path d="M7 2c-2 1-3 3-2 6 1 4 5 9 9 10 2 1 4 0 5-1l-3-3-2 1c-2-1-4-4-5-6l1-2z" fill="var(--ink)"/></svg>
      07-3910 4826
    </li>
    <li>
      <svg viewBox="0 0 24 20" aria-hidden="true"><rect x="7" y="2" width="10" height="16" rx="1.5" fill="none" stroke="var(--ink)" stroke-width="1.6"/><line x1="10" y1="15.5" x2="14" y2="15.5" stroke="var(--ink)" stroke-width="1.4"/></svg>
      0412 587 306
    </li>
    <li>
      <svg viewBox="0 0 24 20" aria-hidden="true"><rect x="7" y="1" width="10" height="6" fill="none" stroke="var(--ink)" stroke-width="1.3"/><rect x="3" y="8" width="18" height="10" rx="1" fill="none" stroke="var(--ink)" stroke-width="1.5"/><line x1="6" y1="12" x2="18" y2="12" stroke="var(--ink)" stroke-width="1.2"/><line x1="6" y1="15" x2="18" y2="15" stroke="var(--ink)" stroke-width="1.2"/></svg>
      07-3910 4827
    </li>
    <li>
      <svg viewBox="0 0 24 20" aria-hidden="true"><rect x="2" y="4" width="20" height="13" fill="none" stroke="var(--ink)" stroke-width="1.6"/><path d="M2 4l10 7 10-7" fill="none" stroke="var(--ink)" stroke-width="1.6"/></svg>
      mirela@msagencies.com.au
    </li>
    <li>
      <svg viewBox="0 0 24 20" aria-hidden="true"><circle cx="12" cy="10" r="8.5" fill="none" stroke="var(--ink)" stroke-width="1.5"/><ellipse cx="12" cy="10" rx="4" ry="8.5" fill="none" stroke="var(--ink)" stroke-width="1.3"/><line x1="3.5" y1="10" x2="20.5" y2="10" stroke="var(--ink)" stroke-width="1.3"/><line x1="12" y1="1.5" x2="12" y2="18.5" stroke="var(--ink)" stroke-width="1.3"/></svg>
      www.msagencies.com.au
    </li>
    <li>
      <svg viewBox="0 0 24 20" aria-hidden="true"><path d="M1 8L12 2l11 6z" fill="var(--ink)"/><rect x="3" y="9" width="18" height="9" fill="var(--ink)"/><rect x="10" y="11" width="4" height="7" fill="var(--paper)"/></svg>
      Unit 3/8 Marlowe Street Eastvale QLD 4170
    </li>
  </ul>
</section>

</body>
</html>
```